CuraNex System Web Page Design

This project is to design 6 pages of a web based medical system for clinics, hospitals, drugs suppliers, general items suppliers, insurance company, laboratories and patients (basically all parties which could be involved in).We want the designs of the browser, button, icon and layout are based on Vex, which is user friendly, looks professional, simple and neat but with powerful functions. We have uploaded few pictures of another system, please do not copy its design because this is not what we are looking for, the pictures are for you to know the elements should be included in our pages. CuraNex web-base system, design 6 pages1. Login PageShould include the following elements-company id with input field-login id with input field-password with input field2. Main Page (Navigation page)Should include the following elements-Appointment-Consultation-Patient-Drugs inventory -General supplies inventory -Laboratory-Suppliers-Insurance-Reports 3. Appointment PageShould include all the the elements in the respective pictures plus the followings-Daily View, Weekly View, Monthly View buttons4. Consultation PageShould include all the the elements in the respective picture5. Patient Page5.1 General information Should include all the the elements in the respective picture5.2 medical history/lab reportsShould include all the the elements in the respective picture plus the followings-Notify patient button-Share report button.
Updated on 28 Nov:
Please stop using Ward Keystone in your designs which is not the name of our system. We have just rename our system to CuraNex, please take note.
We need the system to look professional not playful, do not use too many colors and playful icons.
professional users

```html
<!DOCTYPE html>
<html lang="en">
<head>
<meta charset="utf-8">
<title>CuraNex System (Consultation)</title>
<link href="https://fonts.googleapis.com/css2?family=Arimo:wght@400;700&display=swap" rel="stylesheet">
<style>
:root{
  --bg:#ececec;
  --panel:#ffffff;
  --sidebar:#e7eaee;
  --sidebar-line:#a9b0b8;
  --titlebar-top:#e6e6e6;
  --titlebar-bottom:#b9b9b9;
  --text:#1e1e1e;
  --muted:#9a9a9a;
  --alert:#e8322c;
  --btn-grey:#a9a9a9;
  --btn-blue-top:#5aa4ea;
  --btn-blue-bottom:#2f7fd4;
  --head:#d4d4d4;
  --rule:#c8c8c8;
  --label:#7b8088;
}
*{box-sizing:border-box;margin:0;padding:0}
html,body{width:1200px;height:675px;overflow:hidden}
body{font-family:"Arimo",Helvetica,Arial,sans-serif;color:var(--text);background:var(--bg);position:relative;font-size:12.3px}
.titlebar{position:absolute;left:0;top:0;width:1200px;height:51px;background:linear-gradient(var(--titlebar-top),var(--titlebar-bottom));border-bottom:1px solid #8f8f8f}
.lights{position:absolute;left:8px;top:5px;display:flex;gap:7px}
.lights span{width:11px;height:11px;border-radius:50%;border:1px solid rgba(0,0,0,.25)}
.lights .close{background:#ec5f56}.lights .min{background:#f3bd3b}.lights .max{background:#5fc84a}
.nav-arrows{position:absolute;left:8px;top:22px;width:47px;height:19px;border:1px solid #8c8c8c;border-radius:4px;background:linear-gradient(#fafafa,#d8d8d8);display:flex}
.nav-arrows span{flex:1;display:flex;align-items:center;justify-content:center}
.nav-arrows span+span{border-left:1px solid #9a9a9a}
.window-title{position:absolute;left:0;right:0;top:21px;text-align:center;font-size:11.4px;color:#3a3a3a}
.search{position:absolute;left:1023px;top:22px;width:169px;height:20px;border:1px solid #8c8c8c;border-radius:10px;background:#fff}
.sidebar{position:absolute;left:0;top:51px;width:167px;height:624px;background:var(--sidebar);border-right:1px solid var(--sidebar-line)}
.sidebar h2{font-size:9px;letter-spacing:1px;color:var(--label);font-weight:700;margin:35px 0 5px 9px}
.sidebar li{list-style:none;height:21px;display:flex;align-items:center;padding-left:9px;font-size:12.3px}
.sidebar li svg{width:14px;height:14px;margin-right:8px}
.sidebar li.active{background:linear-gradient(#5aa4ea,#3b86d6);color:#fff}
.card{position:absolute;background:var(--panel);border-radius:2px}
.lines{line-height:17.6px;font-size:12.3px}
.btn{position:absolute;height:26px;width:102px;border-radius:2px;background:var(--btn-grey);color:#fff;font-size:11.4px;display:flex;align-items:center;justify-content:center}
.btn.primary{background:linear-gradient(var(--btn-blue-top),var(--btn-blue-bottom))}
.alert{color:var(--alert)}
.panel-head{height:32px;background:var(--head);display:flex;align-items:center;padding-left:17px;font-size:10.5px}
.row{border-bottom:1px solid var(--rule);padding:10px 17px}
.row:last-child{border-bottom:none}
.drug .sub{color:var(--muted);margin-top:2px}
</style>
</head>
<body>
<header class="titlebar">
  <div class="lights"><span class="close"></span><span class="min"></span><span class="max"></span></div>
  <div class="nav-arrows">
    <span><svg width="7" height="8"><path d="M6 0L0 4L6 8Z" fill="#666"/></svg></span>
    <span><svg width="7" height="8"><path d="M1 0L7 4L1 8Z" fill="#666"/></svg></span>
  </div>
  <div class="window-title">CuraNex System (Consultation)</div>
  <div class="search">
    <svg width="169" height="18" style="position:absolute;left:0;top:0">
      <circle cx="11" cy="8.5" r="4" fill="none" stroke="#555" stroke-width="1.4"/>
      <line x1="14" y1="11.5" x2="17" y2="14.5" stroke="#555" stroke-width="1.6"/>
      <circle cx="156" cy="9" r="5" fill="#b5b5b5"/>
      <path d="M154 7l4 4M158 7l-4 4" stroke="#fff" stroke-width="1.2"/>
    </svg>
  </div>
</header>

<nav class="sidebar">
  <h2>IMPORTANT LINKS</h2>
  <ul>
    <li><svg viewBox="0 0 14 14"><circle cx="7" cy="7" r="4" fill="none" stroke="#777"/><path d="M2 2l10 10" stroke="#777"/></svg>Allergy</li>
    <li><svg viewBox="0 0 14 14"><rect x="1" y="3" width="12" height="9" rx="1" fill="#777"/><path d="M7 5v5M4.5 7.5h5" stroke="#fff" stroke-width="1.5"/></svg>Medical His.</li>
    <li><svg viewBox="0 0 14 14"><path d="M2 12l8-8M9 2l3 3" stroke="#777" stroke-width="2"/></svg>Immunization</li>
    <li class="active"><svg viewBox="0 0 14 14"><rect x="4" y="1" width="6" height="9" rx="1" fill="#fff"/><path d="M7 10v3" stroke="#fff" stroke-width="1.5"/></svg>Glucose Data</li>
    <li><svg viewBox="0 0 14 14"><circle cx="9" cy="9" r="3" fill="none" stroke="#777" stroke-width="1.4"/><path d="M2 2v4a3 3 0 0 0 6 0V2" fill="none" stroke="#777" stroke-width="1.4"/></svg>BP Data</li>
    <li><svg viewBox="0 0 14 14"><rect x="2" y="6" width="10" height="7" fill="#777"/><rect x="5" y="1" width="2" height="5" fill="#777"/></svg>Laboratory</li>
    <li><svg viewBox="0 0 14 14"><rect x="2" y="1" width="10" height="12" fill="none" stroke="#777"/><path d="M4 4h6M4 7h6M4 10h6" stroke="#777"/></svg>Image, Doc.</li>
    <li><svg viewBox="0 0 14 14"><circle cx="7" cy="2.5" r="1.2" fill="#777"/><circle cx="7" cy="7" r="1.2" fill="#777"/><circle cx="7" cy="11.5" r="1.2" fill="#777"/></svg>Others</li>
  </ul>
</nav>

<section class="card patient" style="left:207px;top:74px;width:266px;height:238px">
  <div class="lines" style="position:absolute;left:27px;top:24px">
    000001<br>A00000(1) MALE<br>LEE KA WING<br>Age: 22 Years<br>Mob: 91234508,<br>Tel: 23456781
  </div>
  <div class="btn primary" style="left:27px;top:140px">Add</div>
  <div class="btn" style="left:137px;top:140px">Edit</div>
  <div class="btn" style="left:27px;top:175px">Delete</div>
</section>

<div class="card" style="left:509px;top:75px;width:232px;height:26px"></div>
<div class="btn" style="left:755px;top:75px">View</div>

<section class="card alerts" style="left:509px;top:111px;width:348px;height:201px">
  <div class="lines alert" style="position:absolute;left:26px;top:21px">
    (28/06/2010) BP: 161,102 P:83<br>(ALLERGY) ANTIBIOTICS<br>ASPIRIN 100 MG<br>ASPIRIN 300 MG<br>(MEDICAL HISTORY) Hypertension
  </div>
</section>

<section class="card address" style="left:893px;top:74px;width:265px;height:238px">
  <div class="lines" style="position:absolute;left:26px;top:24px">
    Flat P, 24/F<br>Harbour View Court<br>Eastbay Terrace
  </div>
  <div class="btn primary" style="left:26px;top:140px">Add</div>
  <div class="btn" style="left:136px;top:140px">Label</div>
  <div class="btn" style="left:26px;top:175px">Delete</div>
</section>

<section class="card notes" style="left:207px;top:347px;width:572px;height:192px">
  <div class="panel-head">28 June 2010</div>
  <div class="row lines" style="height:88px">
    Diagnosis :: Heart Disease, Other<br>Complaint :: CHest Symptom / Complaint<br>Findings :: Chest Pain NOS<br>Action :: Blood Test
  </div>
  <div class="row" style="height:37px"></div>
  <div class="row" style="height:35px"></div>
</section>

<section class="card prescriptions" style="left:811px;top:347px;width:347px;height:192px">
  <div class="panel-head">28 June 2010</div>
  <div class="row drug" style="height:53px"><div>PARACETAMOL 250MG</div><div class="sub">DOS:1 FEQ:E6-PRN DAY:3 QTY:12.00</div></div>
  <div class="row drug" style="height:54px"><div>OSELVIR 75MG</div><div class="sub">DOS:1 FEQ:2 DAY:5 QTY:10:00</div></div>
  <div class="row drug" style="height:53px"><div>BROMEX SYR</div><div class="sub">DOS:5ML FEQ:3 DAY:3 QTY:45.00</div></div>
</section>

<div class="btn primary" style="left:207px;top:575px">Next</div>
<div class="btn" style="left:328px;top:575px">Appoint</div>
<div class="btn" style="left:450px;top:575px">Search</div>
<div class="btn" style="left:571px;top:575px">Patient</div>
<div class="btn" style="left:692px;top:575px">Recall</div>
<div class="btn" style="left:814px;top:575px">Bill, Doc.</div>
<div class="btn" style="left:935px;top:575px">Document</div>
<div class="btn" style="left:1056px;top:575px">Write</div>
<div class="btn" style="left:207px;top:619px">Print</div>
<div class="btn" style="left:328px;top:619px">Main</div>
</body>
</html>
```